Beyond The Ledger Double Sided DL Flyer

We need a double sided flyer that we provide to a Real Estate agent for leeds. It should provide our basic services as well as a modern look and feel. The brochure should incorporate our Brand colors and have a graphic that centres around money and property. I have included a couple of pictures that we like (but have not yet purchased from PIXVAULT) as an indication of the type of picture we like.

WE need to also show the Beyond The Ledger brand and have our Phone / address's and email details.

Target Market(s)

Realestate clients (Property Investors)

Industry/Entity Type

Financial Planning

Requirements
Must have
• Picture on Front (maybe the logo on back)
• Please incorporate existing logo colours.

```html
<!DOCTYPE html>
<html lang="en">
<head>
<meta charset="utf-8">
<title>Beyond The Ledger – DL Flyer</title>
<link href="https://fonts.googleapis.com/css2?family=Oswald:wght@400;500;600&family=Roboto:wght@400;500;700&display=swap" rel="stylesheet">
<style>
  :root{
    --green:#8cc63f;
    --green-dark:#6fa92a;
    --ink:#2b2b2b;
    --charcoal:#333;
    --paper:#ffffff;
    --mist:#ececec;
    --stage:#d9dde0;
  }
  *{box-sizing:border-box;margin:0;padding:0}
  html,body{width:1200px;height:1200px;overflow:hidden}
  body{background:var(--stage);font-family:'Roboto',sans-serif;color:var(--ink);position:relative}
  .flyer{position:absolute;top:135px;width:440px;height:930px;background:var(--paper);overflow:hidden;box-shadow:0 10px 30px rgba(0,0,0,.18)}
  .flyer--front{left:120px}
  .flyer--back{left:640px}
  .abs{position:absolute}
  .hero-photo{left:0;top:0;width:440px;height:300px}
  .hero-photo--property{background:linear-gradient(135deg,#e9e2d8 0%,#d8cfc4 40%,#bcd6a0 75%,#8fbf5a 100%)}
  .hero-photo--coins{background:radial-gradient(circle at 65% 55%,#f3d27a 0%,#c98a2a 30%,#5a3a18 65%,#1e150c 100%)}
  .wave{left:0;width:440px}
  .brand{display:flex;align-items:center;gap:8px;font-family:'Oswald',sans-serif;font-weight:600;color:var(--green);text-transform:uppercase;letter-spacing:.5px}
  .brand__dot{width:14px;height:14px;border-radius:50%;background:var(--green)}
  .photo-circle{border-radius:50%;border:8px solid var(--green);box-shadow:0 0 0 6px #fff,0 0 0 7px var(--ink)}
  .headline{left:30px;top:420px;font-family:'Oswald',sans-serif;font-size:40px;line-height:1.1;text-transform:uppercase}
  .headline__lead{color:var(--green);font-weight:500}
  .headline__tail{color:var(--ink);font-weight:400}
  .services{left:0;top:545px;width:440px;height:300px;background:linear-gradient(180deg,#efefef,#e4e4e4)}
  .services__pill{left:22px;top:20px;width:320px;background:var(--charcoal);color:#fff;border-radius:22px;padding:8px 18px;font-size:13px;font-weight:700;text-transform:uppercase;line-height:1.3}
  .services__pill b{color:var(--green)}
  .services__list{left:22px;top:92px;list-style:none;font-size:12px;line-height:1.8;color:var(--ink)}
  .services__list li{display:flex;align-items:center;gap:7px}
  .tick{width:12px;height:12px;flex:none}
  .portrait{border-radius:6px}
  .portrait--advisor-f{left:302px;top:90px;width:124px;height:210px;background:linear-gradient(180deg,#e6d3a8 0%,#c9b79d 35%,#6f6f73 70%,#55565a 100%)}
  .footer-url{left:0;width:440px;text-align:center;font-size:14px;font-weight:500;color:var(--ink)}
  .advisor{left:0;top:392px;width:440px;text-align:center}
  .advisor__role{font-size:16px;letter-spacing:1px;border-top:1px solid var(--ink);display:inline-block;padding:4px 24px 0}
  .advisor__name{font-family:'Oswald',sans-serif;font-weight:500;font-size:20px;color:var(--green);text-transform:uppercase;border-bottom:1px solid var(--ink);display:inline-block;padding:0 24px 2px}
  .hours{left:50px;top:470px;width:340px;height:62px;border:2px solid var(--ink);border-radius:31px;text-align:center;background:#fff}
  .hours__label{font-family:'Oswald',sans-serif;font-weight:500;color:var(--green);font-size:17px;text-transform:uppercase;background:#fff;display:inline-block;padding:0 8px;margin-top:-13px}
  .hours__time{font-size:18px;margin-top:0}
  .mini-photo{width:90px;height:90px;border-radius:50%}
  .mini-photo--savings{left:95px;top:550px;background:radial-gradient(circle,#f1ede4,#b8a78a)}
  .mini-photo--planning{left:200px;top:565px;background:radial-gradient(circle,#e7edf3,#8ea5bf)}
  .contact{left:40px;top:672px;list-style:none;font-size:13px;line-height:1.35}
  .contact li{display:flex;gap:10px;align-items:flex-start;margin-bottom:10px}
  .contact svg{width:15px;height:15px;flex:none;margin-top:1px}
  .portrait--client{left:292px;top:640px;width:138px;height:200px;background:linear-gradient(180deg,#e2c5a4 0%,#cfb9a3 30%,#8c8f94 60%,#6d7075 100%)}
</style>
</head>
<body>

<!-- Front panel -->
<section class="flyer flyer--front">
  <div class="abs hero-photo hero-photo--property" role="img" aria-label="Hands holding a small wooden house above coin stacks with green seedlings"></div>
  <svg class="abs wave" style="top:230px" width="440" height="90" viewBox="0 0 440 90">
    <path d="M0 50 Q220 75 440 10 L440 90 L0 90 Z" fill="var(--green)"/>
    <path d="M0 62 Q220 88 440 24 L440 90 L0 90 Z" fill="var(--ink)"/>
    <path d="M0 68 Q220 94 440 30 L440 90 L0 90 Z" fill="#fff"/>
  </svg>
  <div class="abs photo-circle" style="left:250px;top:240px;width:170px;height:170px;background:radial-gradient(circle at 40% 40%,#9fcf6a,#3f6e2a 70%,#2b3f22)" role="img" aria-label="Watering can pouring onto a plant growing from coins beside a small house"></div>
  <div class="abs brand" style="left:30px;top:345px;font-size:21px"><span class="brand__dot"></span>Beyond The Ledger</div>
  <h1 class="abs headline">
    <span class="headline__lead">Build your business &amp;</span><br>
    <span class="headline__tail">Grow your wealth</span>
  </h1>
  <div class="abs services">
    <div class="abs services__pill"><b>Accountants &amp; Financial Advisors</b><br>who specialise in:</div>
    <ul class="abs services__list">
      <li><svg class="tick" viewBox="0 0 12 12"><circle cx="6" cy="6" r="5.2" fill="none" stroke="var(--green)" stroke-width="1.2"/><path d="M3.5 6.2l1.7 1.7 3.3-3.4" fill="none" stroke="var(--green)" stroke-width="1.4"/></svg>Negative Gearing &amp; Investment Properties</li>
      <li><svg class="tick" viewBox="0 0 12 12"><circle cx="6" cy="6" r="5.2" fill="none" stroke="var(--green)" stroke-width="1.2"/><path d="M3.5 6.2l1.7 1.7 3.3-3.4" fill="none" stroke="var(--green)" stroke-width="1.4"/></svg>Property &amp; Capital Gains Tax Minimisation</li>
      <li><svg class="tick" viewBox="0 0 12 12"><circle cx="6" cy="6" r="5.2" fill="none" stroke="var(--green)" stroke-width="1.2"/><path d="M3.5 6.2l1.7 1.7 3.3-3.4" fill="none" stroke="var(--green)" stroke-width="1.4"/></svg>Self-Managed Superannuation Funds (SMSF)</li>
      <li><svg class="tick" viewBox="0 0 12 12"><circle cx="6" cy="6" r="5.2" fill="none" stroke="var(--green)" stroke-width="1.2"/><path d="M3.5 6.2l1.7 1.7 3.3-3.4" fill="none" stroke="var(--green)" stroke-width="1.4"/></svg>Small Business &amp; Personal Taxation</li>
      <li><svg class="tick" viewBox="0 0 12 12"><circle cx="6" cy="6" r="5.2" fill="none" stroke="var(--green)" stroke-width="1.2"/><path d="M3.5 6.2l1.7 1.7 3.3-3.4" fill="none" stroke="var(--green)" stroke-width="1.4"/></svg>Investment Advice &amp; Risk Insurances</li>
    </ul>
    <div class="abs portrait portrait--advisor-f" role="img" aria-label="Smiling businesswoman in a grey suit with arms folded"></div>
  </div>
  <svg class="abs wave" style="top:800px" width="440" height="130" viewBox="0 0 440 130">
    <path d="M0 10 Q220 70 440 40 L440 130 L0 130 Z" fill="#fff"/>
    <path d="M0 10 Q220 70 440 40" fill="none" stroke="var(--ink)" stroke-width="3"/>
    <path d="M0 95 Q220 130 440 70 L440 130 L0 130 Z" fill="var(--green)"/>
  </svg>
  <div class="abs footer-url" style="top:868px">www.beyondtheledger.com.au</div>
</section>

<!-- Back panel -->
<section class="flyer flyer--back">
  <div class="abs hero-photo hero-photo--coins" role="img" aria-label="Hand placing a coin on stacks of coins against a golden sunset"></div>
  <svg class="abs wave" style="top:230px" width="440" height="90" viewBox="0 0 440 90">
    <path d="M0 30 Q220 95 440 30 L440 90 L0 90 Z" fill="var(--green)"/>
    <path d="M0 44 Q220 110 440 44 L440 90 L0 90 Z" fill="#f4f4f4"/>
  </svg>
  <div class="abs" style="left:0;top:310px;width:440px;height:500px;background:linear-gradient(180deg,#f4f4f4,#ebebeb)"></div>
  <div class="abs brand" style="left:0;width:440px;justify-content:center;top:335px;font-size:24px"><span class="brand__dot"></span>Beyond The Ledger</div>
  <div class="abs advisor">
    <div class="advisor__role">ADVISOR</div><br>
    <div class="advisor__name">Nathan Carver</div>
  </div>
  <div class="abs hours">
    <div class="hours__label">Office Hours:</div>
    <div class="hours__time">Monday to Friday 9am – 5pm</div>
  </div>
  <div class="abs mini-photo mini-photo--savings" role="img" aria-label="Alarm clock beside rising coin stacks"></div>
  <div class="abs mini-photo mini-photo--planning" role="img" aria-label="Hands working a calculator over financial charts"></div>
  <ul class="abs contact">
    <li><svg viewBox="0 0 16 16"><path d="M8 1a5 5 0 0 0-5 5c0 4 5 9 5 9s5-5 5-9a5 5 0 0 0-5-5z" fill="var(--green)"/><circle cx="8" cy="6" r="1.8" fill="#fff"/></svg><span>Suite 8 / 41 Harbour Street<br>Tarrow NSW 2100</span></li>
    <li><svg viewBox="0 0 16 16"><path d="M4 1.5l2.5 3-1.5 1.6c.8 1.8 2.2 3.2 4 4l1.6-1.5 3 2.5-1.3 2.4C7.5 13.4 2.6 8.5 1.6 3z" fill="var(--green)"/></svg><span>(02) 5550 1842</span></li>
    <li><svg viewBox="0 0 16 16"><rect x="1" y="3" width="14" height="10" rx="1.5" fill="var(--green)"/><path d="M1.5 4l6.5 5 6.5-5" fill="none" stroke="#fff" stroke-width="1.3"/></svg><span>hello@beyondtheledger.com.au</span></li>
    <li><svg viewBox="0 0 16 16"><circle cx="8" cy="8" r="7" fill="var(--green)"/><path d="M1 8h14M8 1c-3 3.5-3 10.5 0 14M8 1c3 3.5 3 10.5 0 14" fill="none" stroke="#fff" stroke-width="1"/></svg><span>www.beyondtheledger.com.au</span></li>
  </ul>
  <div class="abs portrait portrait--client" role="img" aria-label="Delighted businessman in a grey suit holding a fan of banknotes"></div>
  <svg class="abs wave" style="top:810px" width="440" height="120" viewBox="0 0 440 120">
    <path d="M0 20 Q200 -5 440 60 L440 120 L0 120 Z" fill="#fff"/>
    <path d="M0 20 Q200 -5 440 60" fill="none" stroke="var(--green)" stroke-width="8"/>
    <path d="M0 95 Q220 120 440 90 L440 120 L0 120 Z" fill="var(--green)"/>
  </svg>
  <div class="abs footer-url" style="top:865px">www.beyondtheledger.com.au</div>
</section>

</body>
</html>
```